Cards and stuff KLP Stone Ridge Construction
Stone Ridge Construction
Cards and stuff KLP Stone Ridge Construction - Construction
Creative Brief
Professional
Marcus Tolley
Owner
812 Linfield Dr
office@stoneridgebuild.example
Don't want address on cards
Surprise me

```html
<!DOCTYPE html>
<html lang="en">
<head>
<meta charset="utf-8">
<title>Stone Ridge Construction – Stationery</title>
<link rel="stylesheet" href="https://fonts.googleapis.com/css2?family=Oswald:wght@700&family=Open+Sans:wght@400;600&display=swap">
<style>
:root{
  --stage:#7c7c7c;
  --paper:#ffffff;
  --ink:#333333;
  --muted:#8a8a8a;
  --red:#c3141b;
  --red-dark:#5e0508;
  --black:#151515;
  --charcoal:#2b2b2b;
}
*{margin:0;padding:0;box-sizing:border-box}
html,body{width:1200px;height:269px;overflow:hidden}
body{background:var(--stage);font-family:"Open Sans",Arial,sans-serif;color:var(--ink);position:relative}
.piece{position:absolute;box-shadow:0 2px 5px rgba(0,0,0,.35);overflow:hidden}
.mark{font-family:"Oswald",Arial,sans-serif;font-weight:700;color:var(--red);letter-spacing:1px;line-height:1}
.mark.light{color:var(--paper)}
.tiny{font-size:3.4px;line-height:5px;color:var(--ink)}
.micro{font-size:2.6px;line-height:3.6px;color:var(--muted)}

/* business cards */
.card-front{left:12px;top:40px;width:98px;height:60px;background:linear-gradient(#f4f4f4,#d9d9d9);display:flex;flex-direction:column;align-items:center;justify-content:center}
.card-front .mark{font-size:20px}
.card-front .firm{font-size:4px;color:var(--muted);margin-top:2px}
.card-front-name{position:absolute;left:14px;top:103px;font-size:5px;color:#eee}
.card-back{left:12px;top:150px;width:98px;height:38px;background:var(--paper)}
.card-back .band{position:absolute;left:0;right:0;bottom:0;height:8px;background:linear-gradient(90deg,var(--red-dark),var(--red))}
.card-back .who{position:absolute;left:8px;top:6px}
.card-back .who b{font-size:5px;display:block;color:var(--ink);margin-bottom:1px}
.card-dark{left:12px;top:196px;width:98px;height:40px;background:var(--black);display:flex;align-items:center;justify-content:center}
.card-dark .mark{font-size:14px}

/* letterheads */
.letter{top:12px;width:132px;height:240px;background:var(--paper);padding:12px 12px}
.letter .head{display:flex;justify-content:flex-start;margin-bottom:22px}
.letter .head .mark{font-size:14px}
.letter p{margin-bottom:5px}
.letter .sign{margin-top:22px;height:8px;width:40px;border-bottom:1px solid var(--muted)}
.letter .foot{position:absolute;left:0;right:0;bottom:0;padding:4px 12px;border-top:2px solid var(--red)}
.letter-a{left:132px}
.letter-b{left:288px}

/* envelopes */
.env{left:444px;width:180px;background:var(--paper)}
.env-a{top:28px;height:62px}
.env-a .mark{position:absolute;left:10px;top:8px;font-size:13px}
.env-a .to{position:absolute;left:80px;top:32px}
.env-b{top:98px;height:44px}
.env-b .mark{position:absolute;left:8px;top:6px;font-size:10px}
.env-b .strip{position:absolute;left:0;right:0;bottom:0;height:5px;background:var(--red)}
.env-c{top:150px;height:40px;background:var(--black);display:flex;align-items:center;justify-content:center}
.env-c .mark{font-size:16px}
.env-d{top:198px;height:30px;background:linear-gradient(90deg,var(--red-dark),var(--red))}

/* compliment and note cards */
.note{left:636px;width:60px;background:var(--paper)}
.note-a{top:24px;height:84px;display:flex;flex-direction:column;align-items:center;padding-top:12px}
.note-a .mark{font-size:13px}
.note-a .line{width:40px;border-bottom:1px solid #ddd;margin-top:10px}
.note-b{top:120px;height:60px;display:flex;align-items:center;justify-content:center}
.note-b .mark{font-size:12px}
.note-c{top:190px;height:46px;background:var(--black);display:flex;align-items:center;justify-content:center}
.note-c .mark{font-size:11px}

/* folder */
.folder-back{left:708px;top:24px;width:150px;height:216px;background:linear-gradient(135deg,var(--charcoal),var(--black))}
.folder-back .pocket{position:absolute;left:0;right:0;bottom:0;height:80px;background:linear-gradient(#3a3a3a,#222)}
.folder-back .slit{position:absolute;left:48px;bottom:56px;width:54px;height:32px;border:1px solid #555}
.folder{left:866px;top:12px;width:322px;height:240px;display:flex}
.folder .panel{flex:1;background:radial-gradient(ellipse at 50% 45%,#e0232a 0%,var(--red) 35%,var(--red-dark) 100%)}
.folder .panel+.panel{border-left:1px solid rgba(0,0,0,.35);display:flex;flex-direction:column;align-items:center;justify-content:center}
.folder .panel .mark{font-size:38px}
.folder .panel .firm{font-size:6px;color:var(--paper);margin-top:4px;letter-spacing:.5px}
</style>
</head>
<body>

<div class="piece card-front">
  <span class="mark">KLP</span>
  <span class="firm">Stone Ridge Construction</span>
</div>
<div class="card-front-name">Marcus Tolley</div>

<div class="piece card-back">
  <div class="who">
    <b>Marcus Tolley</b>
    <span class="micro">Owner</span><br>
    <span class="micro">office@stoneridgebuild.example</span>
  </div>
  <div class="band"></div>
</div>

<div class="piece card-dark"><span class="mark">KLP</span></div>

<div class="piece letter letter-a">
  <div class="head"><span class="mark">KLP</span></div>
  <p class="tiny">Dear Client,</p>
  <p class="tiny">Thank you for choosing our team for your next build. We value quality work and clear plans.</p>
  <p class="tiny">Our crew will contact you soon to confirm the schedule and site details.</p>
  <p class="tiny">Sincerely,</p>
  <div class="sign"></div>
  <p class="tiny">Marcus Tolley</p>
  <div class="foot micro">812 Linfield Dr · office@stoneridgebuild.example</div>
</div>

<div class="piece letter letter-b">
  <div class="head"><span class="mark">KLP</span></div>
  <p class="tiny">Dear Client,</p>
  <p class="tiny">Thank you for choosing our team for your next build. We value quality work and clear plans.</p>
  <p class="tiny">Our crew will contact you soon to confirm the schedule and site details.</p>
  <p class="tiny">Sincerely,</p>
  <div class="sign"></div>
  <p class="tiny">Marcus Tolley</p>
  <div class="foot micro">812 Linfield Dr · office@stoneridgebuild.example</div>
</div>

<div class="piece env env-a">
  <span class="mark">KLP</span>
  <div class="to micro">Stone Ridge Con<br>812 Linfield Dr</div>
</div>
<div class="piece env env-b"><span class="mark">KLP</span><div class="strip"></div></div>
<div class="piece env env-c"><span class="mark light">KLP</span></div>
<div class="piece env env-d"></div>

<div class="piece note note-a"><span class="mark">KLP</span><div class="line"></div><div class="line"></div></div>
<div class="piece note note-b"><span class="mark">KLP</span></div>
<div class="piece note note-c"><span class="mark">KLP</span></div>

<div class="piece folder-back"><div class="pocket"></div><div class="slit"></div></div>

<div class="piece folder">
  <div class="panel"></div>
  <div class="panel">
    <span class="mark light">KLP</span>
    <span class="firm">Stone Ridge Construction</span>
  </div>
</div>

</body>
</html>
```